Business Card and Stationary for KVT Builders
Need standard business card, letterhead, and envelopes to incorporate our new logo
Business Card and Stationary for KVT Builders - Construction
Creative Brief
Simple
Rowan Pelley
Vice President
4621 Brantwell Houston, TX 77031
rowan@kvtbuilders.example
I'm open to layout ideas for all designs. letterhead and envelopes need to be accessible to incorporate microsoft office products.

```html
<!DOCTYPE html>
<html lang="en">
<head>
<meta charset="utf-8">
<title>KVT Builders — Stationery</title>
<link href="https://fonts.googleapis.com/css2?family=Open+Sans:ital,wght@0,400;0,600;0,700;0,800&display=swap" rel="stylesheet">
<style>
  :root{
    --brand:#3b3a9c;
    --brand-dark:#2c2b80;
    --wave-grey:#a3a3b2;
    --paper:#ffffff;
    --ink:#3a3a48;
    --muted:#8a8a98;
    --line:#c9c9d4;
    --stage:#ececef;
  }
  *{box-sizing:border-box;margin:0;padding:0}
  html,body{width:1200px;height:542px;overflow:hidden}
  body{background:var(--stage);font-family:"Open Sans",Arial,sans-serif;color:var(--ink);position:relative}

  .sheet{position:absolute;background:var(--paper);box-shadow:0 2px 6px rgba(0,0,0,.18);overflow:hidden}
  .wave{position:absolute;left:0;bottom:0;width:100%;display:block}

  .brand{display:flex;align-items:center;gap:4px;font-weight:800;color:var(--brand);line-height:1}
  .brand-dot{border-radius:50%;background:var(--brand);flex:none}
  .brand-tagline{font-weight:600;color:var(--muted);letter-spacing:.2px}
  .on-blue .brand{color:#fff}
  .on-blue .brand-dot{background:#fff}
  .on-blue .brand-tagline{color:#d6d6f0}

  /* business cards */
  .card-front{left:24px;top:29px;width:168px;height:103px}
  .card-front .logo{position:absolute;left:10px;top:10px}
  .card-front .brand{font-size:12px}
  .card-front .brand-dot{width:8px;height:8px}
  .card-front .brand-tagline{font-size:3.5px;margin-top:2px}
  .card-front .contact{position:absolute;left:10px;top:46px;font-size:4px;line-height:1.5}
  .card-front .person{position:absolute;right:12px;top:50px;text-align:right}
  .card-front .person-name{font-size:6px;font-weight:700;color:var(--brand)}
  .card-front .person-title{font-size:4px;color:var(--muted)}

  .card-back{left:211px;top:29px;width:168px;height:103px;background:var(--brand)}
  .card-back .logo{position:absolute;left:0;right:0;top:34px;display:flex;flex-direction:column;align-items:center}
  .card-back .brand{font-size:15px}
  .card-back .brand-dot{width:9px;height:9px}
  .card-back .brand-tagline{font-size:4px;margin-top:3px}

  /* envelope front */
  .env-front{left:24px;top:156px;width:360px;height:168px}
  .env-front .logo{position:absolute;left:14px;top:14px}
  .env-front .brand{font-size:16px}
  .env-front .brand-dot{width:10px;height:10px}
  .env-front .brand-tagline{font-size:4.5px;margin-top:2px}
  .env-front .return{position:absolute;left:14px;top:118px;font-size:4.5px;line-height:1.5}

  /* envelope back */
  .env-back{left:24px;top:348px;width:360px;height:168px}
  .env-back .logo{position:absolute;left:0;right:0;top:56px;display:flex;flex-direction:column;align-items:center}
  .env-back .brand{font-size:16px}
  .env-back .brand-dot{width:10px;height:10px}
  .env-back .brand-tagline{font-size:4.5px;margin-top:2px}

  /* letterhead */
  .letterhead{left:432px;top:12px;width:336px;height:518px}
  .letterhead .logo{position:absolute;left:22px;top:16px}
  .letterhead .brand{font-size:17px}
  .letterhead .brand-dot{width:11px;height:11px}
  .letterhead .brand-tagline{font-size:4.5px;margin-top:2px}
  .letter{position:absolute;left:22px;right:26px;top:86px;font-size:4.6px;line-height:1.55}
  .letter p{margin-bottom:7px}
  .letter .para{text-align:justify}
  .sheet-footer{position:absolute;left:22px;right:22px;bottom:8px;display:flex;justify-content:space-between;font-size:4.4px;color:#fff;z-index:2}

  /* fax */
  .fax{left:816px;top:12px;width:360px;height:518px}
  .fax .logo{position:absolute;left:22px;top:16px}
  .fax .brand{font-size:17px}
  .fax .brand-dot{width:11px;height:11px}
  .fax .brand-tagline{font-size:4.5px;margin-top:2px}
  .fax-frame{position:absolute;left:22px;right:22px;top:62px;height:370px;border:1px solid var(--line)}
  .fax-header{height:20px;background:var(--brand);display:flex;justify-content:flex-end;align-items:center;gap:6px;padding-right:14px;color:#fff;font-weight:700;font-size:8px;letter-spacing:.5px}
  .fax-tab{position:absolute;left:12px;width:26px;height:12px;background:var(--brand);color:#fff;font-size:4.6px;font-weight:700;display:flex;align-items:center;justify-content:center}
  .fax-field{position:absolute;left:64px;right:16px;height:12px;border:1px solid var(--line);font-size:4.6px;color:var(--muted);display:flex;align-items:center;padding-left:6px}
  .fax-box{position:absolute;left:64px;right:16px;border:1px solid var(--line)}
</style>
</head>
<body>

<!-- Business card front -->
<section class="sheet card-front">
  <div class="logo">
    <div class="brand"><span class="brand-dot"></span>KVT Builders</div>
    <div class="brand-tagline">Quality Construction Since Day One</div>
  </div>
  <div class="contact">
    <div>4621 Brantwell Houston, TX 77031</div>
    <div>Tel 713-555-0142</div>
    <div>Fax 713-555-0143</div>
    <div>rowan@kvtbuilders.example</div>
  </div>
  <div class="person">
    <div class="person-name">Rowan Pelley</div>
    <div class="person-title">Vice President</div>
  </div>
  <svg class="wave" viewBox="0 0 168 20" height="20" preserveAspectRatio="none">
    <path d="M0 12 C50 0 110 4 168 10 L168 20 L0 20Z" fill="var(--wave-grey)"/>
    <path d="M0 16 C60 6 110 8 168 14 L168 20 L0 20Z" fill="var(--brand)"/>
  </svg>
</section>

<!-- Business card back -->
<section class="sheet card-back on-blue">
  <div class="logo">
    <div class="brand"><span class="brand-dot"></span>KVT Builders</div>
    <div class="brand-tagline">Quality Construction Since Day One</div>
  </div>
</section>

<!-- Envelope front -->
<section class="sheet env-front">
  <div class="logo">
    <div class="brand"><span class="brand-dot"></span>KVT Builders</div>
    <div class="brand-tagline">Quality Construction Since Day One</div>
  </div>
  <div class="return">
    <div>4621 Brantwell Houston, TX 77031</div>
    <div>kvtbuilders.example</div>
  </div>
  <svg class="wave" viewBox="0 0 360 32" height="32" preserveAspectRatio="none">
    <path d="M0 14 C120 -2 240 2 360 18 L360 32 L0 32Z" fill="var(--wave-grey)"/>
    <path d="M0 22 C120 6 240 10 360 24 L360 32 L0 32Z" fill="var(--brand)"/>
  </svg>
</section>

<!-- Envelope back -->
<section class="sheet env-back on-blue">
  <svg viewBox="0 0 360 168" width="360" height="168" style="position:absolute;left:0;top:0">
    <path d="M0 168 L150 92 L210 92 L360 168" fill="none" stroke="var(--line)" stroke-width="1"/>
    <path d="M0 38 C100 58 260 58 360 38 L360 112 L180 128 L0 112Z" fill="var(--wave-grey)"/>
    <path d="M0 44 C100 64 260 64 360 44 L360 106 L180 122 L0 106Z" fill="var(--brand)"/>
  </svg>
  <div class="logo">
    <div class="brand"><span class="brand-dot"></span>KVT Builders</div>
    <div class="brand-tagline">Quality Construction Since Day One</div>
  </div>
</section>

<!-- Letterhead -->
<section class="sheet letterhead">
  <div class="logo">
    <div class="brand"><span class="brand-dot"></span>KVT Builders</div>
    <div class="brand-tagline">Quality Construction Since Day One</div>
  </div>
  <div class="letter">
    <p>March 4, 2024</p>
    <p>Mr. Daniel Ortiz<br>Ortiz Retail Group<br>1200 Main Street<br>Houston, TX 77002</p>
    <p>Dear Mr. Ortiz,</p>
    <p class="para">Thank you for the opportunity to present our proposal for your new commercial facility. Our team has reviewed the site plans and prepared a schedule that meets your goals.</p>
    <p class="para">We manage every phase of construction in house, from early design through final inspection, so you have one point of contact and clear costs at every step of the build.</p>
    <p class="para">Please review the enclosed documents and let us know a convenient time to meet. We look forward to working with you.</p>
    <p>Sincerely,<br><br>Rowan Pelley</p>
  </div>
  <svg class="wave" viewBox="0 0 336 40" height="40" preserveAspectRatio="none">
    <path d="M0 12 C110 -2 230 4 336 16 L336 40 L0 40Z" fill="var(--wave-grey)"/>
    <path d="M0 20 C110 6 230 10 336 22 L336 40 L0 40Z" fill="var(--brand)"/>
  </svg>
  <div class="sheet-footer"><span>4621 Brantwell Houston, TX 77031</span><span>kvtbuilders.example</span></div>
</section>

<!-- Fax cover -->
<section class="sheet fax">
  <div class="logo">
    <div class="brand"><span class="brand-dot"></span>KVT Builders</div>
    <div class="brand-tagline">Quality Construction Since Day One</div>
  </div>
  <div class="fax-frame">
    <div class="fax-header">
      <svg width="12" height="8" viewBox="0 0 12 8"><path d="M0 4 H10 M7 1 L10 4 L7 7" stroke="#fff" stroke-width="1.6" fill="none"/></svg>
      <span>FAX</span>
    </div>
    <div class="fax-tab" style="top:34px">TO</div>
    <div class="fax-field" style="top:34px">To</div>
    <div class="fax-field" style="top:52px">From</div>
    <div class="fax-field" style="top:70px">Company</div>
    <div class="fax-field" style="top:88px">Fax</div>
    <div class="fax-tab" style="top:106px">FROM</div>
    <div class="fax-field" style="top:106px">Phone</div>
    <div class="fax-field" style="top:124px">Re</div>
    <div class="fax-tab" style="top:146px">NOTE</div>
    <div class="fax-box" style="top:146px;height:206px"></div>
  </div>
  <svg class="wave" viewBox="0 0 360 40" height="40" preserveAspectRatio="none">
    <path d="M0 12 C120 -2 240 4 360 16 L360 40 L0 40Z" fill="var(--wave-grey)"/>
    <path d="M0 20 C120 6 240 10 360 22 L360 40 L0 40Z" fill="var(--brand)"/>
  </svg>
  <div class="sheet-footer"><span>4621 Brantwell Houston, TX 77031</span><span>kvtbuilders.example</span></div>
</section>

</body>
</html>
```